Stationary design for IT Consultancy
Stationary Design (Business Cards - Letter Heads - Envelopes - Presentation Folders - Power Point)
Stationary design for IT Consultancy - Information Technology
Creative Brief
Use standard fonts
Optional fonts can be used
Professional
Dean Marlow
Technical Director
14 Brindle Works Oakfield Lane Stoneham Wexshire WX7 2QP
dean.marlow@pivotal-nsg.net
www.pivotal-nsg.net

```html
<!DOCTYPE html>
<html lang="en">
<head>
<meta charset="utf-8">
<title>Pivotal Network Services Group – Stationery</title>
<link rel="stylesheet" href="https://fonts.googleapis.com/css2?family=Montserrat:wght@400;600;700&display=swap">
<style>
:root{
  --brand:#3b57a8;
  --brand-soft:#5a73bb;
  --paper:#ffffff;
  --backdrop:#e9eaec;
  --ink:#5a5f6b;
}
*{margin:0;padding:0;box-sizing:border-box}
html,body{width:1200px;height:936px;overflow:hidden;background:var(--backdrop);font-family:"Montserrat",sans-serif}
.canvas{position:relative;width:1200px;height:936px}
.sheet{position:absolute;background:var(--paper);overflow:hidden;box-shadow:0 2px 6px rgba(0,0,0,.12)}
.band{position:absolute;left:0;bottom:0;width:100%;display:block}
.brand{display:flex;align-items:center;gap:6px;color:var(--brand)}
.brand-mark{width:10px;height:10px;background:var(--brand)}
.brand-name{font-weight:700;letter-spacing:.06em;line-height:1}
.brand-tag{color:var(--brand);font-weight:600;letter-spacing:.28em;font-size:6px;margin-top:3px}
.small{color:var(--ink);font-size:5px;line-height:1.5}

.letterhead{left:177px;top:63px;width:393px;height:544px}
.letterhead .brand-block{position:absolute;left:22px;top:24px}
.letterhead .brand-name{font-size:15px}
.letterhead .contact{position:absolute;right:22px;top:24px;width:120px}

.folder{left:633px;top:38px;width:460px;height:574px}
.folder .brand-block{position:absolute;left:0;right:0;top:240px;text-align:center}
.folder .brand{justify-content:center;gap:10px}
.folder .brand-mark{width:20px;height:20px}
.folder .brand-name{font-size:38px}
.folder .brand-tag{font-size:11px;margin-top:6px;letter-spacing:.32em}

.card{left:46px;width:177px;height:101px;border-radius:4px}
.card-front{top:648px}
.card-back{top:759px;background:var(--brand)}
.card-front .brand-block{position:absolute;left:10px;top:10px}
.card-front .brand-mark{width:6px;height:6px}
.card-front .brand-name{font-size:10px}
.card-front .brand-tag{font-size:4px}
.card-front .person{position:absolute;right:10px;top:32px;text-align:right}
.card-front .person b{display:block;color:var(--brand);font-size:6px;margin-bottom:1px}
.card-url{position:absolute;left:12px;color:#fff;font-size:5px;letter-spacing:.15em;line-height:1}
.card-front .card-url{bottom:8px}
.card-back .card-url{bottom:12px}

.envelope-front{left:263px;top:648px;width:430px;height:227px}
.envelope-front .brand-block{position:absolute;left:18px;top:18px}
.envelope-front .brand-name{font-size:14px}
.envelope-front .address{position:absolute;left:18px;top:52px;width:200px}

.envelope-back{left:736px;top:663px;width:428px;height:212px}
.envelope-back .flap{position:absolute;left:0;top:0;width:100%;height:74px;background:var(--brand)}
.envelope-back .flap-url{position:absolute;left:0;right:0;top:31px;text-align:center;color:#fff;font-size:8px;letter-spacing:.3em;font-weight:600}
</style>
</head>
<body>
<main class="canvas">

  <section class="sheet letterhead">
    <div class="brand-block">
      <div class="brand"><span class="brand-mark"></span><span class="brand-name">PIVOTAL</span></div>
      <div class="brand-tag">NETWORK SERVICES GROUP</div>
    </div>
    <div class="contact small">
      14 Brindle Works Oakfield Lane Stoneham Wexshire WX7 2QP<br>
      T: 01632 960418<br>
      dean.marlow@pivotal-nsg.net<br>
      www.pivotal-nsg.net
    </div>
    <svg class="band" viewBox="0 0 393 110" height="110" preserveAspectRatio="none">
      <path d="M0 40 Q196 -10 393 40 L393 110 L0 110Z" fill="var(--brand)"/>
    </svg>
  </section>

  <section class="sheet folder">
    <div class="brand-block">
      <div class="brand"><span class="brand-mark"></span><span class="brand-name">PIVOTAL</span></div>
      <div class="brand-tag">NETWORK SERVICES GROUP</div>
    </div>
    <svg class="band" viewBox="0 0 460 100" height="100" preserveAspectRatio="none">
      <path d="M0 36 Q230 -10 460 36 L460 100 L0 100Z" fill="var(--brand)"/>
    </svg>
  </section>

  <section class="sheet card card-front">
    <div class="brand-block">
      <div class="brand"><span class="brand-mark"></span><span class="brand-name">PIVOTAL</span></div>
      <div class="brand-tag">NETWORK SERVICES GROUP</div>
    </div>
    <div class="person small"><b>Dean Marlow</b>Technical Director<br>dean.marlow@pivotal-nsg.net</div>
    <svg class="band" viewBox="0 0 177 24" height="24" preserveAspectRatio="none">
      <path d="M0 6 Q88 -2 177 6 L177 24 L0 24Z" fill="var(--brand)"/>
    </svg>
    <div class="card-url">www.pivotal-nsg.net</div>
  </section>

  <section class="sheet card card-back">
    <div class="card-url">www.pivotal-nsg.net</div>
  </section>

  <section class="sheet envelope-front">
    <div class="brand-block">
      <div class="brand"><span class="brand-mark"></span><span class="brand-name">PIVOTAL</span></div>
      <div class="brand-tag">NETWORK SERVICES GROUP</div>
    </div>
    <div class="address small">14 Brindle Works Oakfield Lane Stoneham<br>Wexshire WX7 2QP · T: 01632 960418</div>
    <svg class="band" viewBox="0 0 430 70" height="70" preserveAspectRatio="none">
      <path d="M0 26 Q215 -8 430 26 L430 70 L0 70Z" fill="var(--brand)"/>
    </svg>
  </section>

  <section class="sheet envelope-back">
    <div class="flap"></div>
    <div class="flap-url">WWW.PIVOTAL-NSG.NET</div>
  </section>

</main>
</body>
</html>
```